Need Business Card ASAP

We need a business card design for a meeting coming up in a few days. The company name is Harwick Development and Construction and the logo is attached. Something clean, cool, and contemporary that we can get to a printer right away. Attached is the business card for Molvar Energy, an affiliated company, which we like. Instead of the hawk on the back, you could use the attached "D". We'll also be needing matching letterhead in the near future, so ideas for that are welcome.

```html
<!DOCTYPE html>
<html lang="en">
<head>
<meta charset="utf-8">
<title>Harwick Development and Construction – Business Card Options</title>
<link rel="stylesheet" href="https://fonts.googleapis.com/css2?family=Source+Sans+3:wght@400;600;700&display=swap">
<style>
  :root {
    --gold: #b5ab72;
    --gold-light: #e4e0c8;
    --ink: #231f20;
    --text: #3a3a3a;
    --white: #ffffff;
    --backdrop-light: #c49462;
    --backdrop-dark: #6e4a2b;
  }
  * { box-sizing: border-box; margin: 0; padding: 0; }
  html, body { width: 1200px; height: 823px; overflow: hidden; }
  body { font-family: "Source Sans 3", "Myriad Pro", sans-serif; }

  .board {
    position: relative;
    width: 1200px;
    height: 823px;
    overflow: hidden;
  }
  .board__backdrop {
    position: absolute;
    inset: 0;
    background: radial-gradient(ellipse at 45% 40%, var(--backdrop-light) 0%, #a87645 55%, var(--backdrop-dark) 100%);
  }
  .option-label {
    position: absolute;
    top: 52px;
    width: 200px;
    margin-left: -100px;
    text-align: center;
    color: var(--white);
    font-size: 32px;
    font-weight: 400;
  }

  .card {
    position: absolute;
    width: 513px;
    height: 293px;
    border-radius: 13px;
    overflow: hidden;
  }
  .card--front { background: var(--white); top: 112px; }
  .card--option-1 { left: 52px; }
  .card--option-2 { left: 623px; }

  .brand-block {
    position: absolute;
    left: 53px;
    top: 25px;
    width: 148px;
    height: 189px;
    display: flex;
    flex-direction: column;
    align-items: center;
    justify-content: center;
    gap: 16px;
  }
  .brand-block__square {
    width: 96px;
    height: 96px;
    background: linear-gradient(135deg, var(--gold) 0%, var(--gold-light) 100%);
  }
  .brand-block__name {
    color: var(--ink);
    font-size: 15px;
    font-weight: 600;
    line-height: 1.2;
    text-align: center;
  }

  .divider {
    position: absolute;
    left: 225px;
    top: 30px;
    width: 2px;
    height: 195px;
    background: linear-gradient(to bottom, #d8d8d8, #8a8a8a 50%, #e6e6e6);
  }

  .contact {
    position: absolute;
    left: 242px;
    top: 34px;
    color: var(--text);
    font-size: 13.5px;
    line-height: 17px;
  }
  .contact__name {
    color: var(--gold);
    font-size: 19px;
    font-weight: 700;
    line-height: 24px;
  }
  .contact__title { margin-bottom: 16px; }
  .contact__address { margin-bottom: 15px; }
  .contact__line { display: flex; align-items: center; gap: 6px; height: 21.5px; }
  .contact__icon { width: 11px; height: 11px; fill: var(--gold); flex: none; }

  .card__band {
    position: absolute;
    left: 0;
    top: 249px;
    width: 513px;
    height: 44px;
  }
  .card__url {
    position: absolute;
    right: 22px;
    top: 264px;
    color: var(--ink);
    font-size: 12.5px;
    font-weight: 700;
    letter-spacing: 1.3px;
  }

  .card--back {
    left: 247px;
    top: 464px;
    background: var(--ink);
  }
  .back-brand {
    position: absolute;
    left: 0;
    right: 0;
    top: 70px;
    display: flex;
    align-items: center;
    justify-content: center;
    gap: 18px;
  }
  .back-brand__square {
    width: 70px;
    height: 70px;
    background: var(--gold);
  }
  .back-brand__name {
    color: var(--white);
    font-size: 30px;
    font-weight: 600;
    line-height: 1.15;
  }
  .card--back .card__url {
    right: 0;
    left: 0;
    top: 275px;
    text-align: center;
    color: var(--white);
    font-size: 12.5px;
  }
</style>
</head>
<body>
<main class="board">
  <div class="board__backdrop" role="img" aria-label="Warm brown leather texture backdrop"></div>

  <div class="option-label" style="left:320px">Option 1</div>
  <div class="option-label" style="left:869px">Option 2</div>

  <!-- Front, option 1 -->
  <section class="card card--front card--option-1">
    <div class="brand-block">
      <div class="brand-block__square"></div>
      <div class="brand-block__name">Harwick Development and Construction</div>
    </div>
    <div class="divider"></div>
    <div class="contact">
      <div class="contact__name">Grant W. Harwick</div>
      <div class="contact__title">Chief Executive Officer</div>
      <div class="contact__address">2217 Orchard Lane<br>Austin, TX 78704</div>
      <div class="contact__line"><svg class="contact__icon" viewBox="0 0 12 12"><path d="M3 1l2 2.5-1 1.2c.6 1.4 1.8 2.6 3.3 3.3l1.2-1L11 9l-1.3 2C5.5 11 1 6.5 1 2.3z"/></svg>(512) 555-0142</div>
      <div class="contact__line"><svg class="contact__icon" viewBox="0 0 12 12"><path d="M3 3h6l2 3v3H1V6zM2 10h2v1H2zM8 10h2v1H8z"/></svg>(512) 555-0178</div>
      <div class="contact__line"><svg class="contact__icon" viewBox="0 0 12 12"><path d="M1 3h10v7H1zM1 3l5 4 5-4" stroke="#fff" stroke-width=".8"/></svg>grant@harwickdevelopment.com</div>
    </div>
    <svg class="card__band" viewBox="0 0 513 44" preserveAspectRatio="none">
      <defs>
        <linearGradient id="band-gold-1" x1="0" x2="1" y1="0" y2="0">
          <stop offset="0" stop-color="#f2f1ea"/>
          <stop offset=".4" stop-color="#e2dfc9"/>
          <stop offset="1" stop-color="#c3b988"/>
        </linearGradient>
      </defs>
      <rect x="0" y="0" width="513" height="44" fill="url(#band-gold-1)"/>
      <polygon points="0,2 225,2 208,18 0,18" fill="var(--ink)"/>
      <polygon points="232,0 248,0 214,30 0,30 0,26 202,26" fill="#ffffff"/>
    </svg>
    <div class="card__url">www.harwickdevelopment.com</div>
  </section>

  <!-- Front, option 2 -->
  <section class="card card--front card--option-2">
    <div class="brand-block">
      <div class="brand-block__square"></div>
      <div class="brand-block__name">Harwick Development and Construction</div>
    </div>
    <div class="divider"></div>
    <div class="contact">
      <div class="contact__name">Grant W. Harwick</div>
      <div class="contact__title">Chief Executive Officer</div>
      <div class="contact__address">2217 Orchard Lane<br>Austin, TX 78704</div>
      <div class="contact__line"><svg class="contact__icon" viewBox="0 0 12 12"><path d="M3 1l2 2.5-1 1.2c.6 1.4 1.8 2.6 3.3 3.3l1.2-1L11 9l-1.3 2C5.5 11 1 6.5 1 2.3z"/></svg>(512) 555-0142</div>
      <div class="contact__line"><svg class="contact__icon" viewBox="0 0 12 12"><path d="M3 3h6l2 3v3H1V6zM2 10h2v1H2zM8 10h2v1H8z"/></svg>(512) 555-0178</div>
      <div class="contact__line"><svg class="contact__icon" viewBox="0 0 12 12"><path d="M1 3h10v7H1zM1 3l5 4 5-4" stroke="#fff" stroke-width=".8"/></svg>grant@harwickdevelopment.com</div>
    </div>
    <svg class="card__band" viewBox="0 0 513 44" preserveAspectRatio="none">
      <defs>
        <linearGradient id="band-gold-2" x1="0" x2="1" y1="0" y2="0">
          <stop offset="0" stop-color="#f2f1ea"/>
          <stop offset=".4" stop-color="#e2dfc9"/>
          <stop offset="1" stop-color="#c3b988"/>
        </linearGradient>
      </defs>
      <rect x="0" y="0" width="513" height="44" fill="url(#band-gold-2)"/>
      <polygon points="0,2 225,2 208,18 0,18" fill="var(--ink)"/>
      <polygon points="232,0 248,0 214,30 0,30 0,26 202,26" fill="#ffffff"/>
    </svg>
    <div class="card__url">www.harwickdevelopment.com</div>
  </section>

  <!-- Back -->
  <section class="card card--back">
    <div class="back-brand">
      <div class="back-brand__square"></div>
      <div class="back-brand__name">Harwick<br>Development and<br>Construction</div>
    </div>
    <div class="card__url">www.harwickdevelopment.com</div>
  </section>
</main>
</body>
</html>
```